Lanterns on the Tide

I need a book cover design for a world history book written for a target audience of high school students and progressive teachers. The book is more balanced towards a world history perspective than a Western-leaning perspective. The first 500 pages deal with the major turning points in world history - from the first hominids that roamed Africa to the end of the Cold War, and the final 100 pages cover the major challenges facing the world today. The book is 95% graphic details, hopefully-engaging stories and needed facts, but there is a bit of sarcasm, verbal irony and asides thrown in to keep the reader's eyes from glossing over. I would need a cover that would appeal to any school teacher, but something that would not scare off students or the average Joe off the street.
Updates

One added note, please leave the bottom right corner -  2" height by 3" width free of text/image for the ISBN code.

As far as a central image goes, it needs to be a dynamic (avoid something readers would readily see elsewhere in their lives) image, or nothing at all.  Also, please justify all text on the back cover to the left side (avoid centering).

Reason: A few people have voiced an interest in having the deadline extended through next weekend to allow for some alterations and also the ability to take advantage of the upcoming holidays. I will take you up on this request. Thank you all again for your submissions. i've seen some very unique takes on the story/tone of the book.

Industry/Entity Type

High School

Requirements
Must have
• I've enclosed a PDF with the text for the front and back cover.

On the back cover, I'd like the quote and the initial question to stand out. I'd like the initial question to be in lower case.

For the spine, I'd like the title font to match the title front from the front cover.

The book cover needs to measure 9.25" by 13.75" with a 1.5" spine. Allow .125 inches for the bleed.

I've attached a Word Document with all the text. The layout is just a suggestion.
Should not have
• I do not want any stock images that I'll need to pay for.

```html
<!DOCTYPE html>
<html lang="en">
<head>
<meta charset="UTF-8">
<title>Lanterns on the Tide — Book Cover</title>
<link href="https://fonts.googleapis.com/css2?family=Source+Serif+4:ital,opsz,wght@0,8..60,700;0,8..60,800;1,8..60,700;1,8..60,800&display=swap" rel="stylesheet">
<style>
  :root {
    --page-bg: #ffffff;
    --cover-red: #e1272e;
    --cover-red-dark: #c91f26;
    --ink-maroon: #2e0707;
    --land-light: #f6eded;
    --land-mid: #f0c4c5;
    --land-blend: #e9797c;
  }

  * { margin: 0; padding: 0; box-sizing: border-box; }

  html, body {
    width: 1200px;
    height: 900px;
    overflow: hidden;
    background: var(--page-bg);
  }

  .canvas {
    position: relative;
    width: 1200px;
    height: 900px;
  }

  .cover {
    position: absolute;
    left: 324px;
    top: 40px;
    width: 552px;
    height: 820px;
    background: var(--cover-red);
    overflow: hidden;
    font-family: "Source Serif 4", Georgia, serif;
    color: var(--ink-maroon);
  }

  .cover__hinge {
    position: absolute;
    left: 0;
    top: 0;
    width: 14px;
    height: 100%;
    background: var(--cover-red-dark);
  }

  .world-collage {
    position: absolute;
    left: 22px;
    top: 185px;
    width: 520px;
    height: 530px;
    border-radius: 50%;
    background: radial-gradient(ellipse at 50% 50%,
      var(--land-light) 0%,
      var(--land-light) 22%,
      var(--land-mid) 45%,
      var(--land-blend) 64%,
      rgba(225, 39, 46, 0) 72%);
  }

  .title {
    position: absolute;
    left: 0;
    top: 44px;
    width: 100%;
    text-align: center;
    font-weight: 800;
    line-height: 0.92;
    letter-spacing: -1px;
  }

  .title__line {
    display: block;
    font-size: 86px;
  }

  .title__line--accent {
    font-style: italic;
    font-size: 74px;
    margin-top: 2px;
  }

  .subtitle {
    position: absolute;
    left: 141px;
    top: 396px;
    width: 280px;
    text-align: center;
    font-style: italic;
    font-weight: 700;
    font-size: 13.5px;
    line-height: 1.25;
    color: var(--ink-maroon);
  }

  .author {
    position: absolute;
    left: 0;
    top: 676px;
    width: 100%;
    text-align: center;
    font-weight: 700;
    font-size: 40px;
    letter-spacing: 0.2px;
  }
</style>
</head>
<body>
  <main class="canvas">
    <section class="cover">
      <div class="cover__hinge"></div>

      <div class="world-collage" role="img" aria-label="Illustration: a circular collage of white country and continent silhouettes scattered on the red cover"></div>

      <h1 class="title">
        <span class="title__line">Lanterns</span>
        <span class="title__line">on the</span>
        <span class="title__line title__line--accent">Tide</span>
      </h1>

      <p class="subtitle">The tales, traditions and<br>turning points of world history and<br>the regional changes of today</p>

      <p class="author">Marcus Ellery</p>
    </section>
  </main>
</body>
</html>
```